Automotive component supplier needs a business card design

We need a business card design for our company called Velmar Global Components Ltd based in the UK. We are a supplier of interior and exterior components to premium car manufacturers such as Corvane Hale, Durrant Fyfe, Maxtorn and Valdessimo. We would like to see a modern business card design that uses the colour blue.

Target Market(s)

Premium automotive car manufacturers.

Industry/Entity Type

Automotive

Contact Information for Business Card

Company Name : Velmar Global Components Limited
Address: 17 Tamsey Yard, Upper Drisk, Warwick, CV31 8RJ, United Kingdom
Web Address : www.velmarparts-example.co.uk

Font styles to use
Other font styles liked:
• Helvetica

Colors
3176b5
0255a3
85acd3
cfdeed
cee9f5
85cae6
34a6d7
0692cd
9bcb3c

Requirements
Must have
• Clear company logo and a mixture of blue colours.
Nice to have
• A high quality modern image.
Should not have
• Multiple colours.

```html
<!DOCTYPE html>
<html lang="en">
<head>
<meta charset="utf-8">
<title>Velmar Global Components – Business Card</title>
<link rel="stylesheet" href="https://fonts.googleapis.com/css2?family=Arimo:wght@400;700&display=swap">
<style>
  :root {
    --backdrop: #9a9a9a;
    --card-black: #050505;
    --card-sheen: #1b1b1b;
    --brand-blue: #34a6d7;
    --rule-blue: #0692cd;
    --text-white: #f2f2f2;
  }
  * { box-sizing: border-box; margin: 0; padding: 0; }
  html, body {
    width: 1200px;
    height: 1200px;
    overflow: hidden;
    background: var(--backdrop);
    font-family: "Arimo", Helvetica, Arial, sans-serif;
  }
  .canvas {
    width: 1200px;
    height: 1200px;
    display: flex;
    align-items: center;
    justify-content: center;
  }
  .business-card {
    position: relative;
    width: 1050px;
    height: 600px;
    background: linear-gradient(160deg, var(--card-sheen) 0%, var(--card-black) 45%, var(--card-black) 100%);
    color: var(--text-white);
    padding: 70px 110px;
  }
  .brand-name {
    display: block;
    font-size: 92px;
    font-weight: 700;
    line-height: 1;
    color: var(--brand-blue);
    letter-spacing: 1px;
  }
  .brand-tagline {
    margin-top: 10px;
    font-size: 26px;
    font-weight: 400;
    letter-spacing: 5px;
    color: var(--brand-blue);
    text-transform: uppercase;
  }
  .rule {
    width: 560px;
    height: 2px;
    background: var(--rule-blue);
  }
  .rule-top { margin: 22px 0 24px; }
  .rule-bottom { margin: 26px 0 22px; }
  .contact { font-style: normal; }
  .contact-line {
    font-size: 27px;
    line-height: 1.3;
  }
  .contact-phone { margin-top: 22px; }
  .contact-email { margin-top: 36px; }
  .website {
    font-size: 46px;
    line-height: 1;
  }
</style>
</head>
<body>
  <main class="canvas">
    <article class="business-card">
      <header class="brand-block">
        <span class="brand-name">VELMAR</span>
        <p class="brand-tagline">Global Components</p>
      </header>
      <div class="rule rule-top"></div>
      <address class="contact">
        <p class="contact-line">17 Tamsey Yard, Upper Drisk, Warwick,</p>
        <p class="contact-line">CV31 8RJ, United Kingdom</p>
        <p class="contact-line contact-phone">0400 118 274</p>
        <p class="contact-line contact-email">info@velmarparts-example.com.au</p>
      </address>
      <div class="rule rule-bottom"></div>
      <p class="website">www.velmarparts-example.co.uk</p>
    </article>
  </main>
</body>
</html>
```